Updated Business Card Design more modern and eye catching

looking for something more dynamic than the sterile card we have now. Please take a look at our web site www.brightmarkfitout.net to see what we do. only looking for the front side of the card for now. I've also attached a sample of a card with raised spot uv ink - it might be cool to incorporate something like that. Card should be bold yet serious. No frilly or scrolly stuff on it.
Updates
Target Market(s)
We do decor and signage for retail business and supermarkets. Our new name should reflect that we're hip but serious.
Contact Information for Business Card
standard business card size - horizontal preferred
Requirements
Must have
- Current logo and colors cannot be changed.
Nice to have
- Must have information shown on existing card but open to some changes. Okay to consider spot uv.
Should not have
- Not busy with pictures in the background.

```html
<!DOCTYPE html>
<html lang="en">
<head>
<meta charset="utf-8">
<title>Brightmark Fitout – Business Card</title>
<link href="https://fonts.googleapis.com/css2?family=Exo+2:wght@600;700&family=Roboto:wght@400;500&display=swap" rel="stylesheet">
<style>
  :root {
    --backdrop: #221f1b;
    --card: #ffffff;
    --gold: #a8964a;
    --ink: #111111;
    --muted: #4a4a4a;
  }
  * { margin: 0; padding: 0; box-sizing: border-box; }
  html, body {
    width: 1200px;
    height: 801px;
    overflow: hidden;
    background: var(--backdrop);
  }
  .card {
    position: absolute;
    left: 150px;
    top: 143px;
    width: 900px;
    height: 514px;
    background: var(--card);
    box-shadow: 0 18px 40px rgba(0,0,0,.45);
  }
  .brand {
    position: absolute;
    left: 64px;
    top: 58px;
    display: flex;
    align-items: center;
    gap: 14px;
  }
  .brand-square {
    width: 34px;
    height: 34px;
    background: var(--gold);
  }
  .brand-name {
    font-family: "Exo 2", sans-serif;
    font-weight: 600;
    font-size: 30px;
    letter-spacing: 1px;
    color: var(--gold);
    text-transform: uppercase;
  }
  .person {
    position: absolute;
    left: 64px;
    top: 140px;
  }
  .person-name {
    font-family: "Exo 2", sans-serif;
    font-weight: 700;
    font-size: 36px;
    letter-spacing: 1px;
    line-height: 1;
    text-transform: uppercase;
  }
  .person-name .first { color: var(--gold); }
  .person-name .last { color: var(--ink); }
  .person-title {
    font-family: "Exo 2", sans-serif;
    font-weight: 600;
    font-size: 20px;
    color: var(--muted);
    margin-top: 6px;
  }
  .address {
    position: absolute;
    left: 64px;
    top: 232px;
    font-family: "Roboto", sans-serif;
    font-size: 20px;
    line-height: 1.3;
    color: var(--muted);
  }
  .contacts {
    position: absolute;
    left: 64px;
    top: 300px;
    list-style: none;
    font-family: "Roboto", sans-serif;
    font-size: 20px;
    color: var(--muted);
  }
  .contacts li {
    display: flex;
    align-items: center;
    gap: 10px;
    height: 28px;
  }
  .contacts svg {
    width: 16px;
    height: 16px;
    fill: var(--gold);
    flex: none;
  }
</style>
</head>
<body>
  <section class="card">
    <div class="brand">
      <span class="brand-square"></span>
      <span class="brand-name">Brightmark Fitout</span>
    </div>

    <div class="person">
      <p class="person-name"><span class="first">Dana</span> <span class="last">Morrow</span></p>
      <p class="person-title">Vice-President</p>
    </div>

    <p class="address">4120 Commerce Loop Dr.<br>Port Harbor, FL 34900</p>

    <ul class="contacts">
      <li>
        <svg viewBox="0 0 16 16" aria-hidden="true"><path d="M3.6 1.2 6 3.6 4.8 5.6c.9 2 2.6 3.7 4.6 4.6l2-1.2 2.4 2.4-1.6 2.6C6.6 13.6 2.4 9.4 1 3.8z"/></svg>
        555.204.7310 ext.3
      </li>
      <li>
        <svg viewBox="0 0 16 16" aria-hidden="true"><path d="M4 1h8v14H4zM5.5 2.5v9h5v-9zM7.3 12.5h1.4v1.4H7.3z" fill-rule="evenodd"/></svg>
        555.349.8126
      </li>
      <li>
        <svg viewBox="0 0 16 16" aria-hidden="true"><path d="M1 3h14v10H1zM2.5 4.5 8 8.6l5.5-4.1z" fill-rule="evenodd"/></svg>
        Dana@BrightmarkFitout.net
      </li>
      <li>
        <svg viewBox="0 0 16 16" aria-hidden="true"><circle cx="8" cy="8" r="7"/></svg>
        www.BrightmarkFitout.net
      </li>
    </ul>
  </section>
</body>
</html>
```